Business Card Design

Massage therapy and healthy food
Zenlo Health Massage (business name)

Target Market(s)

Health conscious

Industry/Entity Type

Business

Contact Information for Business Card

0413867205

Font styles to use
Serif

```html
<!DOCTYPE html>
<html lang="en">
<head>
<meta charset="utf-8">
<title>Zenlo Health Massage – Business Card</title>
<link rel="stylesheet" href="https://fonts.googleapis.com/css2?family=Lora:wght@400&family=Pinyon+Script&display=swap">
<style>
  :root {
    --stage: #efeae4;
    --card-white: #ffffff;
    --pink: #e98fc4;
    --pink-soft: #f3bfdc;
    --pink-deep: #e07bb8;
    --teal: #3fc1b0;
    --line-pink: #efb0d4;
    --back-light: #f6d3e8;
    --back-mid: #eaa6cf;
    --back-edge: #d98abb;
    --white: #ffffff;
  }
  * { box-sizing: border-box; margin: 0; padding: 0; }
  html, body {
    width: 1200px; height: 885px; overflow: hidden;
    background: var(--stage);
  }
  .stage {
    position: relative; width: 1200px; height: 885px;
    font-family: "Lora", Georgia, serif;
  }
  .card {
    position: absolute; top: 162px;
    width: 340px; height: 560px;
    border-radius: 16px; overflow: hidden;
    box-shadow: 0 10px 28px rgba(80, 50, 40, 0.18);
  }

  /* Front */
  .card--front { left: 190px; background: var(--card-white); }
  .front__brand { position: absolute; top: 92px; left: 0; right: 0; text-align: center; }
  .brand-name {
    color: var(--pink); font-size: 31px; line-height: 1.12; font-weight: 400;
  }
  .tagline-row {
    display: flex; align-items: center; justify-content: center; gap: 10px;
    margin-top: 8px;
  }
  .tagline-row .rule { width: 34px; height: 1px; background: var(--line-pink); }
  .tagline {
    color: var(--teal); font-size: 11px; letter-spacing: 2.2px;
  }
  .front__person { position: absolute; top: 256px; left: 0; right: 0; text-align: center; }
  .person-name {
    font-family: "Pinyon Script", cursive; color: var(--teal);
    font-size: 40px; line-height: 1.1;
  }
  .person-title { color: var(--pink-soft); font-size: 18px; margin-top: 4px; }
  .front__phone {
    position: absolute; top: 376px; left: 0; right: 0; text-align: center;
    color: var(--teal); font-size: 32px; letter-spacing: 1px;
  }
  .front__band {
    position: absolute; left: 0; right: 0; bottom: 0; height: 78px;
    background: linear-gradient(to bottom, #fbe3f0 0%, var(--pink-soft) 35%, var(--pink) 100%);
  }

  /* Back */
  .card--back {
    left: 670px;
    background: linear-gradient(160deg, var(--back-light) 0%, var(--back-mid) 55%, var(--back-edge) 100%);
  }
  .back__glow {
    position: absolute; inset: 0;
    background: radial-gradient(circle at 45% 42%, rgba(255,255,255,0.35) 0%, rgba(255,255,255,0) 55%);
  }
  .back__brand {
    position: absolute; top: 50%; left: 50%;
    width: 480px; transform: translate(-50%, -50%) rotate(90deg);
    text-align: center; color: var(--white);
  }
  .back__brand .brand-name { color: var(--white); font-size: 40px; line-height: 1.1; }
  .back__brand .tagline-row { margin-top: 10px; }
  .back__brand .tagline-row .rule { width: 48px; background: rgba(255,255,255,0.75); }
  .back__brand .tagline { color: var(--white); font-size: 13px; letter-spacing: 2.6px; }
</style>
</head>
<body>
<main class="stage">
  <section class="card card--front" aria-label="Business card front">
    <div class="front__brand">
      <h1 class="brand-name">Zenlo<br>Health Massage</h1>
      <div class="tagline-row">
        <span class="rule"></span>
        <p class="tagline">Massage therapy and healthy food</p>
        <span class="rule"></span>
      </div>
    </div>
    <div class="front__person">
      <p class="person-name">Employee Name</p>
      <p class="person-title">Employee Title</p>
    </div>
    <p class="front__phone">0413867205</p>
    <div class="front__band"></div>
  </section>

  <section class="card card--back" aria-label="Business card back">
    <div class="back__glow" role="img" aria-label="Soft faint floral decoration in light pink"></div>
    <div class="back__brand">
      <h2 class="brand-name">Zenlo<br>Health Massage</h2>
      <div class="tagline-row">
        <span class="rule"></span>
        <p class="tagline">Massage therapy and healthy food</p>
        <span class="rule"></span>
      </div>
    </div>
  </section>
</main>
</body>
</html>
```